Business card and Stationery for data intelligence company

We need a new design for our business cards and stationery (Business Letter templates and a Quote example on Word, but it MUST work on Google Doc as well).

We are a software company based in Ireland and UK. Our product is "Kovar", data intelligence platform with beautiful visualizations, graph capabilities (things are interconnected), powerful, flexible, it can manage Big Data and Streaming information. It's modern and relatively open source.
Our company will provide data intelligence for law enforcements, pharmaceuticals, and similar high end customers.

We'll launch a new website soon. At the moment it's http://www.kovar-analytics.example if you want to take a look. This is our youtube channel in case you need it to understand what Kovar is: https://www.youtube.com/c/kovaranalyticschannel

We changed the logo so please use the logo I attach here.

We'd like the output to be cool and modern but elegant and "business" at the same time. It should inspire simple sophistication, "unity" "intent" "purpose" yet subtly very advanced and innovative.

The name "Kovar" does NOT refer to sirens (mithological creatures) as well as the warning devices. It means Kinetic Object Vector Analysis Reactor. Please use our logo's colors and if you want to something like the "graph" image.

```html
<!DOCTYPE html>
<html lang="en">
<head>
<meta charset="utf-8">
<title>Kovar — Business Card</title>
<link rel="stylesheet" href="https://fonts.googleapis.com/css2?family=Arimo:wght@400;700&display=swap">
<style>
  :root {
    --stage: #3a3230;
    --card: #141414;
    --card-edge: #1e1e1e;
    --accent: #f4a21c;
    --silver: #b9b9b9;
    --ink: #f2f2f2;
    --muted: #6d6d6d;
  }
  * { box-sizing: border-box; margin: 0; padding: 0; }
  html, body {
    width: 1200px; height: 864px; overflow: hidden;
    background: var(--stage);
    font-family: "Arimo", Arial, sans-serif;
  }
  .stage {
    position: relative; width: 1200px; height: 864px;
    display: flex; align-items: center; justify-content: center; gap: 40px;
  }
  .card {
    position: relative; width: 540px; height: 309px;
    background: var(--card);
    border: 1px solid var(--card-edge);
    box-shadow: 0 14px 30px rgba(0,0,0,.45);
  }
  /* Front */
  .card--front .brand {
    position: absolute; left: 70px; top: 100px;
    display: flex; align-items: center; gap: 18px;
  }
  .brand__dot {
    width: 54px; height: 54px; border-radius: 50%;
    border: 6px solid var(--silver);
  }
  .brand__name {
    font-weight: 700; font-size: 58px; letter-spacing: 6px;
    color: var(--silver); line-height: 1;
  }
  .card--front .web {
    position: absolute; left: 72px; top: 200px;
    font-size: 14px; letter-spacing: 4px; color: var(--muted);
  }
  /* Back */
  .person { position: absolute; left: 36px; top: 34px; }
  .person__name { color: var(--accent); font-weight: 700; font-size: 19px; }
  .person__title { color: var(--silver); font-size: 14px; margin-top: 3px; }
  .contacts { position: absolute; left: 36px; top: 88px; list-style: none; }
  .contacts li {
    display: flex; align-items: center; gap: 9px;
    color: var(--ink); font-size: 13px; line-height: 21px;
  }
  .contacts svg { width: 13px; height: 13px; fill: var(--accent); flex: none; }
  .divider {
    position: absolute; left: 36px; right: 36px; top: 180px;
    height: 1px; background: var(--ink);
  }
  .card--back .brand {
    position: absolute; right: 36px; top: 78px;
    display: flex; align-items: center; gap: 12px;
  }
  .card--back .brand__dot { width: 38px; height: 38px; border-width: 5px; border-color: var(--accent); }
  .card--back .brand__name { font-size: 40px; letter-spacing: 4px; color: var(--accent); }
  .address {
    position: absolute; right: 36px; top: 210px; text-align: right;
    color: var(--ink); font-size: 14px; line-height: 21px;
  }
  .address .web { color: var(--accent); letter-spacing: 3px; margin-top: 6px; display: block; }
</style>
</head>
<body>
<main class="stage">
  <section class="card card--front" aria-label="Card front">
    <div class="brand">
      <span class="brand__dot"></span>
      <span class="brand__name">KOVAR</span>
    </div>
    <p class="web">www.kovar-analytics.example</p>
  </section>

  <section class="card card--back" aria-label="Card back">
    <div class="person">
      <p class="person__name">Marek Doyle</p>
      <p class="person__title">President</p>
    </div>
    <ul class="contacts">
      <li><svg viewBox="0 0 16 16"><path d="M3 1h3l1.5 4-2 1.3a9 9 0 0 0 4.2 4.2L11 8.5l4 1.5v3a2 2 0 0 1-2 2C6.5 15 1 9.5 1 3a2 2 0 0 1 2-2z"/></svg>555 0142 7781</li>
      <li><svg viewBox="0 0 16 16"><path d="M4 0h8a1 1 0 0 1 1 1v14a1 1 0 0 1-1 1H4a1 1 0 0 1-1-1V1a1 1 0 0 1 1-1zm1 2v10h6V2zm3 11a1 1 0 1 0 0 2 1 1 0 0 0 0-2z"/></svg>555 0193 4460</li>
      <li><svg viewBox="0 0 16 16"><path d="M4 1h7v4H4zM2 6h12a1 1 0 0 1 1 1v6a1 1 0 0 1-1 1H2a1 1 0 0 1-1-1V7a1 1 0 0 1 1-1zm2 3v2h8V9z"/></svg>555 0167 2208</li>
      <li><svg viewBox="0 0 16 16"><path d="M1 3h14v10H1zm1.5 1.5L8 9l5.5-4.5z"/></svg>marek@kovar-analytics.example</li>
    </ul>
    <div class="brand">
      <span class="brand__dot"></span>
      <span class="brand__name">KOVAR</span>
    </div>
    <div class="divider"></div>
    <address class="address" style="font-style:normal">
      2417 Harbour Lane<br>
      Kilcarra, NY 11099
      <span class="web">www.kovar-analytics.example</span>
    </address>
  </section>
</main>
</body>
</html>
```